Packaging & Label Design for CDB Products

We are a European CBD company specialising in athletic recovery, sleep improvement and wellness.

We would like the packaging to incorporate our logo and name (and font 'Codec') 'Meridell CBD'. The design must be transferable to all of our products. CBD Oils, Balms, Lip Balm and Vape E-Liquid.

We would like it to be simple but eye-catching and modern. We don't want bright colours. Preferred pallet of muted greys, blacks, white and pastel colours. Geometric concepts, possibly using different colours for each item of the range, we are open to new and fresh ideas (we are seeking you for your experience) and when we find the right design we would likely throw more work in your direction..

Our product range is not complete so the designer must be flexible with some changes and provide files where format can be easily edited by packaging manufacturer. We are also waiting for dimensions for the labels and boxes for several products and will supply the designer with full dimensions of all products once selected.

Oil Box: 2.6 x 9.0 x 2.6 cm (open format 16.7 x 11.6cm)
Labels: 7.8 x 3.3 cm (Front and Back)

Our expected product range will be:
CBD Oil 1000mg
CBD Oil 3000mg
CBD Balm 100mg
CBD Balm 300mg
E-Liquid 500mg
Lip Balm 50mg

We look forward to seeing your ideas.

Best Regards
Meridell CBD

```html
<!DOCTYPE html>
<html lang="en">
<head>
<meta charset="utf-8">
<title>Meridell CBD – Oil Packaging</title>
<link rel="stylesheet" href="https://fonts.googleapis.com/css2?family=Barlow+Condensed:wght@500;700&family=Barlow:wght@400;600&family=Montserrat:wght@500&display=swap">
<style>
  :root {
    --bg: #f1f1f2;
    --charcoal: #2e2e31;
    --bar: #252527;
    --berry: #a9557a;
    --berry-soft: #b9638a;
    --rose-text: #e6a9c2;
    --silver: #d6d6d8;
    --white: #ffffff;
    --muted: #a6a6aa;
  }
  * { margin: 0; padding: 0; box-sizing: border-box; }
  html, body { width: 1200px; height: 971px; overflow: hidden; background: var(--bg); }
  .canvas { position: relative; width: 1200px; height: 971px; }

  .panel { position: absolute; overflow: hidden; }
  .panel svg.panel-bg { position: absolute; inset: 0; width: 100%; height: 100%; }
  .box-side { left: 90px; top: 105px; width: 300px; height: 760px; }
  .box-front { left: 390px; top: 105px; width: 300px; height: 760px; }
  .bottle-label { left: 740px; top: 400px; width: 400px; height: 170px; }

  .brand {
    position: absolute; left: 0; right: 0;
    display: flex; align-items: center; justify-content: center; gap: 10px;
  }
  .brand-dot { border-radius: 50%; background: var(--silver); flex: none; }
  .wordmark {
    font-family: "Montserrat", sans-serif; font-weight: 500;
    color: var(--white); letter-spacing: 0.14em; text-transform: uppercase; white-space: nowrap;
  }
  .box-front .brand { top: 140px; }
  .box-front .brand-dot { width: 18px; height: 18px; }
  .box-front .wordmark { font-size: 21px; }
  .bottle-label .brand { top: 9px; left: 40px; gap: 7px; }
  .bottle-label .brand-dot { width: 10px; height: 10px; }
  .bottle-label .wordmark { font-size: 12px; }

  .headline { position: absolute; font-family: "Barlow Condensed", sans-serif; font-weight: 700; line-height: 0.9; white-space: nowrap; }
  .box-front .percent { top: 305px; right: 30px; font-size: 96px; color: var(--silver); }
  .box-front .natural { top: 410px; right: 30px; font-size: 68px; color: var(--white); }
  .bottle-label .percent { top: 28px; left: 40px; right: 0; text-align: center; font-size: 40px; color: var(--white); }
  .bottle-label .natural { top: 64px; left: 40px; right: 0; text-align: center; font-size: 30px; color: var(--white); }

  .tag-bar {
    position: absolute; background: var(--bar); color: var(--silver);
    font-family: "Barlow Condensed", sans-serif; font-weight: 500; text-align: right; white-space: nowrap;
  }
  .box-front .product-type { top: 474px; right: 30px; width: 220px; font-size: 26px; line-height: 30px; padding-right: 6px; }
  .box-front .spectrum { top: 664px; right: 30px; width: 230px; font-family: "Barlow", sans-serif; font-weight: 400; font-size: 20px; line-height: 28px; text-align: left; padding-left: 8px; letter-spacing: 0.02em; }
  .bottle-label .product-type { top: 94px; left: 152px; width: 120px; font-size: 15px; line-height: 18px; padding-right: 5px; }

  .strength { position: absolute; font-family: "Barlow", sans-serif; font-weight: 400; color: var(--white); white-space: nowrap; }
  .strength small { font-size: 0.62em; }
  .box-front .strength { top: 510px; right: 30px; width: 220px; text-align: center; font-size: 34px; line-height: 40px; }
  .bottle-label .strength { top: 115px; left: 40px; right: 0; text-align: center; font-size: 17px; line-height: 22px; }

  .thc-note { position: absolute; font-family: "Barlow Condensed", sans-serif; font-weight: 700; color: var(--rose-text); white-space: nowrap; }
  .box-front .thc-note { top: 634px; right: 30px; font-size: 18px; }
  .bottle-label .thc-note {
    left: 24px; top: 85px; font-size: 12px; color: var(--white);
    transform: translate(-50%, -50%) rotate(-90deg);
  }

  .volume { position: absolute; font-family: "Barlow", sans-serif; font-weight: 600; color: var(--white); white-space: nowrap; }
  .box-front .volume { top: 704px; right: 30px; width: 230px; text-align: center; font-size: 18px; }
  .bottle-label .volume { top: 143px; left: 40px; right: 0; text-align: center; font-size: 12px; }

  .info-block { position: absolute; left: 24px; width: 250px; font-family: "Barlow", sans-serif; color: var(--muted); font-size: 10px; line-height: 1.6; }
  .info-block h3 { font-size: 9px; font-weight: 600; color: var(--rose-text); margin-bottom: 4px; }
  .info-block.directions { top: 80px; }
  .info-block.ingredients { top: 330px; }

  .web-address {
    position: absolute; left: 30px; top: 680px;
    font-family: "Barlow", sans-serif; font-size: 14px; color: var(--silver);
    transform: translate(-50%, -50%) rotate(-90deg); white-space: nowrap;
  }
</style>
</head>
<body>
<main class="canvas">

  <section class="panel box-side" aria-label="Box side panel">
    <svg class="panel-bg" viewBox="0 0 300 760" preserveAspectRatio="none" aria-hidden="true">
      <rect width="300" height="760" fill="var(--charcoal)"/>
      <polygon points="0,640 300,560 300,760 0,760" fill="var(--berry)"/>
    </svg>
    <div class="info-block directions">
      <h3>Directions</h3>
      <p>Shake well before use. Place one full dropper under the tongue and hold for sixty seconds before swallowing. Take once or twice daily, ideally after training or before sleep. Start with a small serving and increase slowly until you find the amount that suits you best. Store in a cool, dry place away from direct sunlight and keep out of reach of children.</p>
    </div>
    <div class="info-block ingredients">
      <h3>Ingredients</h3>
      <p>Full spectrum hemp extract in organic MCT coconut oil. Cold pressed and lab tested for purity. Not intended to diagnose, treat or cure any disease. Consult a doctor if pregnant.</p>
    </div>
    <div class="web-address">www.meridellcbd.eu</div>
  </section>

  <section class="panel box-front" aria-label="Box front panel">
    <svg class="panel-bg" viewBox="0 0 300 760" preserveAspectRatio="none" aria-hidden="true">
      <rect width="300" height="760" fill="var(--charcoal)"/>
      <polygon points="0,560 300,360 300,760 0,760" fill="var(--berry)"/>
    </svg>
    <div class="brand"><span class="brand-dot"></span><span class="wordmark">Meridell CBD</span></div>
    <div class="headline percent">100%</div>
    <div class="headline natural">NATURAL</div>
    <div class="tag-bar product-type">CBD OIL</div>
    <div class="strength">1000<small>mg</small></div>
    <div class="thc-note">LESS THAN 0.3% &#916;9 THC</div>
    <div class="tag-bar spectrum">FULL SPECTRUM</div>
    <div class="volume">1 oz (30ML)</div>
  </section>

  <section class="panel bottle-label" aria-label="Bottle label">
    <svg class="panel-bg" viewBox="0 0 400 170" preserveAspectRatio="none" aria-hidden="true">
      <rect width="400" height="170" fill="var(--charcoal)"/>
      <polygon points="0,120 400,40 400,170 0,170" fill="var(--berry-soft)"/>
    </svg>
    <div class="thc-note">LESS THAN 0.3% &#916;9 THC</div>
    <div class="brand"><span class="brand-dot"></span><span class="wordmark">Meridell CBD</span></div>
    <div class="headline percent">100%</div>
    <div class="headline natural">NATURAL</div>
    <div class="tag-bar product-type">CBD OIL</div>
    <div class="strength">1000<small>mg</small></div>
    <div class="volume">1 oz (30ML)</div>
  </section>

</main>
</body>
</html>
```